Brochure & Business card design

Looking for a new business card design i want it to be modern and sharp looking i usually order plastic business cards, and i would like to make the colors like the logo teal/charcoal i will like to have our services on icons with words.... our services are
ROOFING GUTTERS PAINTING PRESSURE WASHING EXTERIOR DESIGN & ATTIC VENTILATION. I also want to add my credentials

Target Market(s)

Oregon local market

Industry/Entity Type

Residential Construction

Contact Information for Business Card

Business info, services, number, website

Font styles to use
Serif
Sans Serif

Colors
33b8a4
5c5c5c
ffffff

Requirements
Must have
• Dale Finch
• Cell:
• Office:
• Email:
• Website:
• also i need our social media icons
• Services ROOFING GUTTERS PAINTING PRESSURE WASHING EXTERIOR DESIGN & ATTIC VENTILATION
• -icons for number, web, email, cell
• OR #584312
• Wa #KTRABLD461X7
Nice to have
• -Clean design Front & Back
• -Icons
• -shape House just like logo design
• -First Impression
Should not have
• Not Busy or lost of eye contact

```html
<!DOCTYPE html>
<html lang="en">
<head>
<meta charset="utf-8">
<title>Ridgeline Home Exteriors – Business Card</title>
<link rel="stylesheet" href="https://fonts.googleapis.com/css2?family=Marcellus&family=Lato:wght@400;700&display=swap">
<style>
  :root {
    --teal: #21958a;
    --teal-bright: #33b8a4;
    --charcoal: #5c5c5c;
    --ink: #3e3e3e;
    --dark-band: #4a4a52;
    --white: #ffffff;
    --stage: #3b3c3e;
    --rule: #9a9a9a;
    --badge-red: #d8262c;
    --badge-dark: #111111;
    --band-edge: #c9c9cc;
  }
  * { box-sizing: border-box; margin: 0; padding: 0; }
  html, body { width: 1200px; height: 900px; overflow: hidden; }
  body {
    background: var(--stage);
    font-family: "Marcellus", Georgia, serif;
    color: var(--ink);
    position: relative;
  }
  .card {
    position: absolute;
    left: 250px;
    width: 700px;
    height: 400px;
    background: var(--white);
    border-radius: 26px;
    overflow: hidden;
  }
  .card--front { top: 40px; }
  .card--back { top: 465px; }

  /* front */
  .brand {
    position: absolute;
    top: 52px; left: 150px; width: 400px;
    text-align: center;
  }
  .brand__top {
    display: flex; align-items: center; justify-content: center; gap: 12px;
    font-size: 34px; color: var(--teal); letter-spacing: 2px; line-height: 1.1;
  }
  .brand__mark { width: 22px; height: 22px; background: var(--teal); }
  .brand__sub {
    font-size: 26px; color: var(--teal); letter-spacing: 1px; line-height: 1.2;
  }
  .brand__tagline {
    margin-top: 6px;
    font-size: 14px; letter-spacing: 3px; color: var(--ink);
  }
  .badge { position: absolute; }
  .badge--cert {
    left: 55px; top: 232px; width: 110px; height: 42px;
    background: var(--badge-red); border-radius: 3px;
  }
  .badge--listing {
    right: 45px; top: 105px; width: 110px; height: 44px;
    background: var(--badge-dark); border-radius: 8px;
  }
  .services {
    position: absolute; left: 195px; right: 40px; top: 228px;
    display: grid; grid-template-columns: auto auto auto;
    justify-content: space-between;
    row-gap: 14px;
    list-style: none;
  }
  .services li {
    font-size: 14px; letter-spacing: 1px; color: var(--ink);
    display: flex; align-items: center; gap: 9px;
    white-space: nowrap;
  }
  .services li::before {
    content: ""; width: 6px; height: 6px; border-radius: 50%;
    background: var(--teal); flex: none;
  }
  .band { position: absolute; left: 0; bottom: 0; width: 100%; }

  /* back */
  .person {
    position: absolute; left: 0; right: 0; top: 118px; text-align: center;
  }
  .person__name { font-size: 36px; color: var(--teal); letter-spacing: 1px; }
  .person__role {
    font-size: 18px; color: var(--charcoal); letter-spacing: 1px; margin-top: 2px;
  }
  .rule {
    position: absolute; left: 40px; right: 40px; top: 215px;
    height: 1px; background: var(--rule);
  }
  .contact {
    position: absolute; top: 240px;
    display: flex; flex-direction: column; align-items: center; gap: 6px;
    font-size: 19px; color: var(--ink);
  }
  .contact svg { width: 22px; height: 22px; fill: var(--teal); }
  .contact--cell { left: 55px; }
  .contact--office { left: 290px; }
  .contact--email { right: 40px; }
  .licence {
    position: absolute; bottom: 10px;
    font-family: "Lato", Arial, sans-serif;
    font-size: 15px; letter-spacing: 1px; color: var(--white);
  }
  .licence--or { left: 70px; }
  .licence--wa { right: 30px; }
  .web {
    position: absolute; bottom: 11px; left: 270px; width: 212px; text-align: center;
    font-size: 15px; color: var(--white); letter-spacing: 0.5px; white-space: nowrap;
  }
</style>
</head>
<body>

<section class="card card--front">
  <div class="brand">
    <div class="brand__top"><span class="brand__mark"></span>RIDGELINE</div>
    <div class="brand__sub">HOME EXTERIORS</div>
    <div class="brand__tagline">WHEN QUALITY MATTERS.</div>
  </div>
  <div class="badge badge--listing" role="img" aria-label="Accredited business badge"></div>
  <div class="badge badge--cert" role="img" aria-label="Certified roofing contractor badge"></div>
  <ul class="services">
    <li>ROOFING</li>
    <li>PRESSURE WASHING</li>
    <li>GUTTERS</li>
    <li>PAINTING</li>
    <li>EXTERIOR DESIGN</li>
    <li>ATTIC VENTILATION</li>
  </ul>
  <svg class="band" width="700" height="60" viewBox="0 0 700 60" preserveAspectRatio="none">
    <path d="M0 48 Q 10 30 40 30 L700 30 L700 60 L0 60 Z" fill="var(--teal)"/>
  </svg>
</section>

<section class="card card--back">
  <div class="person">
    <div class="person__name">DALE FINCH</div>
    <div class="person__role">General Manager</div>
  </div>
  <div class="rule"></div>

  <div class="contact contact--cell">
    <svg viewBox="0 0 24 24"><path d="M7 1h10a2 2 0 0 1 2 2v18a2 2 0 0 1-2 2H7a2 2 0 0 1-2-2V3a2 2 0 0 1 2-2zm0 3v14h10V4zm5 15.5a1 1 0 1 0 0 2 1 1 0 0 0 0-2z"/></svg>
    <span>123 456 7890</span>
  </div>
  <div class="contact contact--office">
    <svg viewBox="0 0 24 24"><path d="M6.6 10.8a15.1 15.1 0 0 0 6.6 6.6l2.2-2.2a1 1 0 0 1 1-.25 11.4 11.4 0 0 0 3.6.57 1 1 0 0 1 1 1V20a1 1 0 0 1-1 1A17 17 0 0 1 3 4a1 1 0 0 1 1-1h3.5a1 1 0 0 1 1 1c0 1.250.2 2.450.57 3.57a1 1 0 0 1-.25 1z"/></svg>
    <span>123 456 7890</span>
  </div>
  <div class="contact contact--email">
    <svg viewBox="0 0 24 24"><path d="M2 5h20v14H2zm2 2v.5l8 5 8-5V7l-8 5z"/></svg>
    <span>info@ridgelinexteriors.com</span>
  </div>

  <svg class="band" width="700" height="46" viewBox="0 0 700 46" preserveAspectRatio="none">
    <rect x="0" y="10" width="700" height="36" fill="var(--teal)"/>
    <path d="M245 10 L500 10 Q 488 12 485 46 L260 46 Q 258 14 245 10 Z" fill="var(--dark-band)"/>
    <path d="M245 10 L252 10 Q 266 14 268 46 L260 46 Q 258 14 245 10 Z" fill="var(--band-edge)"/>
    <path d="M500 10 L492 10 Q 480 12 477 46 L485 46 Q 488 12 500 10 Z" fill="var(--band-edge)"/>
  </svg>
  <span class="licence licence--or">OR #584312</span>
  <span class="web">www.ridgelinexteriors.com</span>
  <span class="licence licence--wa">Wa #KTRABLD461X7</span>
</section>

</body>
</html>
```